Mine Engineering Consultancy specializing in
* Pit optimization
* Mine Design
* Scheduling
* Mine Rehabilitation

Industry/Entity Type

Mining

Contact Information for Business Card

RVT Mining Pty Ltd
Derek Holloway
Director/Principle Mining Engineer
Mobile 0413582961
Email derek.holloway@rvtmining-example.com

```html
<!DOCTYPE html>
<html lang="en">
<head>
<meta charset="utf-8">
<title>RVT Mining Pty Ltd – Business Card</title>
<link rel="stylesheet" href="https://fonts.googleapis.com/css2?family=Tinos:wght@400&display=swap">
<style>
  :root {
    --stage: #d4d4d4;
    --card-white: #f4f4f4;
    --card-white-edge: #e9e9e9;
    --brand-blue: #0a6bbf;
    --back-blue: #0570c1;
    --rule-grey: #555555;
    --text-grey: #3c3c3c;
    --band-grey: #7d7d7d;
    --white: #ffffff;
  }
  * { box-sizing: border-box; margin: 0; padding: 0; }
  html, body { width: 1200px; height: 941px; overflow: hidden; }
  body {
    background: var(--stage);
    font-family: "Tinos", "Times New Roman", serif;
    position: relative;
  }
  .card {
    position: absolute;
    width: 520px;
    height: 300px;
    box-shadow: 0 6px 18px rgba(0,0,0,0.18);
    overflow: hidden;
  }
  /* Front */
  .card-front {
    left: 50px; top: 320px;
    background: linear-gradient(135deg, var(--card-white), var(--card-white-edge));
  }
  .front-brand {
    position: absolute; left: 34px; top: 48px;
    display: flex; align-items: center; gap: 10px;
  }
  .brand-dot {
    width: 14px; height: 14px; border-radius: 50%;
    background: var(--brand-blue);
  }
  .brand-name {
    color: var(--brand-blue);
    font-size: 30px;
    line-height: 1;
  }
  .front-rule {
    position: absolute; left: 58px; right: 34px; top: 90px;
    height: 1px; background: var(--rule-grey);
  }
  .front-services {
    position: absolute; left: 58px; top: 98px;
    font-size: 13px; color: var(--text-grey); letter-spacing: 0.2px;
  }
  .person {
    position: absolute; left: 34px; top: 206px;
  }
  .person-name {
    color: var(--brand-blue); font-size: 21px; letter-spacing: 0.5px;
  }
  .person-title {
    color: var(--text-grey); font-size: 13px; margin-top: 2px;
  }
  .contact {
    position: absolute; right: 34px; top: 150px;
    text-align: right; font-size: 13px; color: var(--text-grey); line-height: 1.7;
  }
  .contact-label { color: var(--brand-blue); }
  .front-band {
    position: absolute; left: 0; bottom: 0; width: 520px; height: 40px;
  }
  /* Back */
  .card-back {
    left: 630px; top: 320px;
    background: var(--back-blue);
    color: var(--white);
  }
  .back-brand {
    position: absolute; left: 40px; top: 70px;
    display: flex; align-items: center; gap: 12px;
  }
  .back-brand .brand-dot { background: var(--white); width: 16px; height: 16px; }
  .back-brand .brand-name { color: var(--white); font-size: 38px; }
  .back-rule {
    position: absolute; left: 68px; right: 0; top: 128px;
    height: 1px; background: var(--white);
  }
  .back-services {
    position: absolute; right: 40px; top: 150px;
    list-style: none; text-align: right;
    font-size: 16px; line-height: 1.55;
  }
</style>
</head>
<body>
  <section class="card card-front" aria-label="Business card front">
    <div class="front-brand">
      <span class="brand-dot"></span>
      <span class="brand-name">RVT Mining Pty Ltd</span>
    </div>
    <div class="front-rule"></div>
    <p class="front-services">Pit optimization · Mine Design · Scheduling · Mine Rehabilitation</p>
    <div class="contact">
      <p><span class="contact-label">T:</span> 0413582961</p>
      <p><span class="contact-label">E:</span> derek.holloway@rvtmining-example.com</p>
    </div>
    <div class="person">
      <p class="person-name">DEREK HOLLOWAY</p>
      <p class="person-title">Director / Principle Mining Engineer</p>
    </div>
    <svg class="front-band" viewBox="0 0 520 40" aria-hidden="true">
      <polygon points="290,40 290,28 300,22 520,22 520,40" fill="var(--band-grey)"/>
      <polygon points="0,40 0,30 282,30 282,22 300,22 290,30 290,40" fill="var(--brand-blue)"/>
    </svg>
  </section>

  <section class="card card-back" aria-label="Business card back">
    <div class="back-brand">
      <span class="brand-dot"></span>
      <span class="brand-name">RVT Mining Pty Ltd</span>
    </div>
    <div class="back-rule"></div>
    <ul class="back-services">
      <li>Pit optimization</li>
      <li>Mine Design</li>
      <li>Scheduling</li>
      <li>Mine Rehabilitation</li>
    </ul>
  </section>
</body>
</html>
```